IT COMPANYcutting edge tec business card

we are IT company that building any apps.
we need business card in japanese and english
You don’t have to include all information in front one you can attach part of that information to back-side
company name : 株式会社かすみ鳥 (MOSSLARK Inc.)
concept : cutting-edge technology
role : 取締役 (director)
name : 河 泰林 (Ha Taerimmu)
post number : 168-0037
address : 東京都世田谷区北霞台5-08-44 (5-08-44, Kitakasumidai, Setagaya Ku, Tokyo To, 168-0037, Japan)
Tel:+81-3-5917-2843
Mobile:+81-80-7263-5518
Email : taerimha@fieldoflark.com
website : www.fieldoflark.com

we dont have logo so please make it as well
we also looking for designer who can make homapage design.

Designs look the same

Low design quality

Contact Information for Business Card

cutting-edge design and modern for IT

Font styles to use
Sans Serif

Colors
34a6d7
33b8a4
6092c4
3377b5
886aae
6b449b
b868aa
a64599

Requirements
Must have
• Simple but designed

```html
<!DOCTYPE html>
<html lang="ja">
<head>
<meta charset="utf-8">
<title>MOSSLARK Inc. – Business Card</title>
<link href="https://fonts.googleapis.com/css2?family=Nunito+Sans:wght@400;600;700&family=Noto+Sans+JP:wght@400;500;700&display=swap" rel="stylesheet">
<style>
  :root {
    --backdrop: #6b6b6b;
    --card: #ffffff;
    --shape-edge: #4f8fd3;
    --grad-start: #5898e8;
    --grad-end: #70cde0;
    --accent: #4cb6e2;
    --ink: #555a63;
  }
  * { margin: 0; padding: 0; box-sizing: border-box; }
  html, body {
    width: 1200px; height: 991px; overflow: hidden;
    background: var(--backdrop);
    font-family: "Nunito Sans", "Noto Sans JP", sans-serif;
  }
  .sheet { position: relative; width: 1200px; height: 991px; }
  .card {
    position: absolute; top: 345px;
    width: 540px; height: 302px;
    background: var(--card);
    border-radius: 14px;
    overflow: hidden;
    box-shadow: 0 6px 16px rgba(0,0,0,.35);
  }
  .card--front { left: 40px; }
  .card--back { left: 620px; }
  .card__shape { position: absolute; inset: 0; }

  .brand {
    position: absolute; left: 205px; top: 116px;
    color: #fff;
  }
  .brand__row { display: flex; align-items: center; gap: 14px; }
  .brand__mark { width: 34px; height: 34px; background: #fff; border-radius: 6px; }
  .brand__name { font-weight: 600; font-size: 34px; line-height: 40px; letter-spacing: 1px; }
  .brand__ja {
    margin: 8px 0 0 48px;
    font-weight: 600; font-size: 14px; line-height: 18px; letter-spacing: 3px;
  }

  .seal {
    position: absolute; left: 118px; top: 104px;
    width: 88px; height: 88px; border-radius: 50%;
    background: #fff;
  }
  .contact { position: absolute; left: 252px; top: 42px; color: var(--ink); }
  .contact__name { color: var(--accent); font-weight: 700; font-size: 18px; line-height: 22px; }
  .contact__name-ja { margin-left: 10px; font-size: 16px; letter-spacing: 2px; }
  .contact__role { font-size: 12.5px; line-height: 16px; margin-bottom: 12px; }
  .contact__list { list-style: none; margin-bottom: 12px; }
  .contact__list li {
    display: flex; align-items: center; gap: 10px;
    font-size: 12.5px; line-height: 18px;
  }
  .contact__list svg { width: 12px; height: 12px; flex: none; }
  .contact__address { font-size: 12.5px; line-height: 18px; font-style: normal; }
  .contact__address-ja { margin-top: 4px; font-size: 12px; line-height: 18px; }
</style>
</head>
<body>
<main class="sheet">

  <section class="card card--front" aria-label="Card front">
    <svg class="card__shape" viewBox="0 0 540 302" aria-hidden="true">
      <defs>
        <linearGradient id="front-grad" x1="0" y1="0" x2="1" y2="1">
          <stop offset="0" stop-color="var(--grad-start)"/>
          <stop offset="1" stop-color="var(--grad-end)"/>
        </linearGradient>
      </defs>
      <polygon points="205,-30 108,82 108,240 222,335 580,335 580,-30"
               fill="var(--shape-edge)" stroke="var(--shape-edge)" stroke-width="20" stroke-linejoin="round"/>
      <polygon points="227,-30 130,82 130,240 244,335 580,335 580,-30"
               fill="url(#front-grad)" stroke="url(#front-grad)" stroke-width="20" stroke-linejoin="round"/>
    </svg>
    <div class="brand">
      <div class="brand__row"><span class="brand__mark"></span><span class="brand__name">MOSSLARK</span></div>
      <p class="brand__ja">株式会社かすみ鳥</p>
    </div>
  </section>

  <section class="card card--back" aria-label="Card back">
    <svg class="card__shape" viewBox="0 0 540 302" aria-hidden="true">
      <defs>
        <linearGradient id="back-grad" x1="1" y1="0" x2="0" y2="1">
          <stop offset="0" stop-color="var(--grad-start)"/>
          <stop offset="1" stop-color="var(--grad-end)"/>
        </linearGradient>
      </defs>
      <polygon points="-30,-30 80,-30 172,52 172,250 78,335 -30,335"
               fill="var(--shape-edge)" stroke="var(--shape-edge)" stroke-width="20" stroke-linejoin="round"/>
      <polygon points="-30,-30 60,-30 152,52 152,250 58,335 -30,335"
               fill="url(#back-grad)" stroke="url(#back-grad)" stroke-width="20" stroke-linejoin="round"/>
    </svg>
    <div class="seal"></div>

    <div class="contact">
      <h1 class="contact__name">HA TAERIMMU<span class="contact__name-ja">河 泰林</span></h1>
      <p class="contact__role">DIRECTOR ／ 取締役</p>
      <ul class="contact__list">
        <li><svg viewBox="0 0 12 12"><path d="M3 1 L5 3.5 L4 5 Q5.5 7 7 8 L8.5 7 L11 9 L9.5 11 Q4 10 1 2.5 Z" fill="var(--accent)"/></svg>+81-3-5917-2843</li>
        <li><svg viewBox="0 0 12 12"><rect x="3" y="1" width="6" height="10" rx="1.2" fill="none" stroke="var(--accent)" stroke-width="1.4"/></svg>+81-80-7263-5518</li>
        <li><svg viewBox="0 0 12 12"><rect x="1" y="2.5" width="10" height="7" fill="var(--accent)"/><path d="M1 2.5 L6 6.5 L11 2.5" fill="none" stroke="#fff" stroke-width="1"/></svg>TAERIMHA@FIELDOFLARK.COM</li>
        <li><svg viewBox="0 0 12 12"><g fill="none" stroke="var(--accent)" stroke-width="1"><circle cx="6" cy="6" r="5"/><ellipse cx="6" cy="6" rx="2.2" ry="5"/><path d="M1 6 H11 M2 3.5 H10 M2 8.5 H10"/></g></svg>WWW.FIELDOFLARK.COM</li>
      </ul>
      <address class="contact__address">
        5-08-44, KITAKASUMIDAI<br>
        SETAGAYA KU, TOKYO TO<br>
        168-0037, JAPAN
        <p class="contact__address-ja">〒168-0037 東京都世田谷区北霞台5-08-44</p>
      </address>
    </div>
  </section>

</main>
</body>
</html>
```